Thornwell Building Company - advertisement poster

I am looking to print some canvas signs to advertise my general contracting company, Thornwell Building Company. The sign will measure 6' long x 3' high so the size should match that ratio. I already have a logo icon, which is the Letter 'T' and some trees that I would like to incorporate, see attached. I would also like the to have the following information listed:
1) phone number: 472-555-0188
2) email: thornwellbuildingcompany@mailvero.com
3) website: thornwellbuildingcompany.com
4) Lic#4620385
5) I want to use this text: "BUILD WITH THE T-CREW!"

The ad should be relatively simple and clean. Black and Green are my company colors. I am open to creative ideas!

Target Market(s)

People looking to renovate their homes

Industry/Entity Type

Construction

Colors
59FF00
82FF00
B8FF75
E3FFCB
F4FFEA

Requirements
Must have
• Must have my company logo
Should not have
• No photos or complex graphics

```html
<!DOCTYPE html>
<html lang="en">
<head>
<meta charset="UTF-8">
<title>Thornwell Building Company – Advertisement Poster</title>
<link rel="stylesheet" href="https://fonts.googleapis.com/css2?family=Ubuntu:wght@400;500;700&display=swap">
<style>
  :root {
    --ink: #1f1f1f;
    --panel-dark: #1e1e1e;
    --brand-green: #6bb842;
    --brand-green-light: #7cc653;
    --accent-green: #6fc33f;
    --white: #ffffff;
    --backdrop: #ececec;
  }
  * { box-sizing: border-box; margin: 0; padding: 0; }
  html, body {
    width: 1200px;
    height: 1000px;
    overflow: hidden;
    background: var(--backdrop);
    font-family: "Ubuntu", Arial, sans-serif;
  }
  .canvas {
    position: relative;
    width: 1200px;
    height: 1000px;
    display: flex;
    align-items: center;
    justify-content: center;
  }
  .poster {
    position: relative;
    width: 1200px;
    height: 600px;
    display: flex;
  }
  .brand-panel {
    width: 530px;
    height: 100%;
    background: var(--panel-dark);
    display: flex;
    flex-direction: column;
    align-items: center;
    justify-content: center;
    gap: 22px;
  }
  .brand-mark {
    width: 46px;
    height: 46px;
    background: var(--brand-green);
  }
  .brand-name {
    color: var(--white);
    font-weight: 700;
    text-align: center;
    text-transform: uppercase;
    line-height: 1.1;
  }
  .brand-name .line-main {
    display: block;
    font-size: 60px;
    letter-spacing: 1px;
  }
  .brand-name .line-sub {
    display: block;
    font-size: 26px;
    letter-spacing: 6px;
    margin-top: 6px;
  }
  .message-panel {
    position: relative;
    flex: 1;
    height: 100%;
    background: linear-gradient(180deg, var(--brand-green-light) 0%, var(--brand-green) 100%);
    color: var(--ink);
  }
  .headline {
    position: absolute;
    top: 40px;
    left: 60px;
    right: 50px;
    text-align: right;
  }
  .headline .lead {
    display: block;
    font-size: 62px;
    font-weight: 500;
    line-height: 1;
    text-align: center;
  }
  .headline .crew {
    display: block;
    font-size: 112px;
    font-weight: 700;
    line-height: 1;
    letter-spacing: 1px;
    text-align: center;
    margin-top: 8px;
  }
  .phone-box {
    position: absolute;
    top: 246px;
    left: 73px;
    width: 512px;
    height: 120px;
    background: var(--panel-dark);
    display: flex;
    align-items: center;
    justify-content: center;
    gap: 18px;
  }
  .phone-box svg { width: 40px; height: 40px; }
  .phone-number {
    color: var(--accent-green);
    font-size: 58px;
    font-weight: 700;
    letter-spacing: 1px;
  }
  .contact-list {
    position: absolute;
    top: 418px;
    left: 73px;
    list-style: none;
  }
  .contact-list li {
    display: flex;
    align-items: center;
    gap: 12px;
    font-size: 25px;
    font-weight: 700;
    height: 43px;
  }
  .contact-list svg { width: 28px; height: 28px; flex: none; }
  .license {
    position: absolute;
    top: 534px;
    left: 0;
    width: 100%;
    padding-left: 0;
    text-align: center;
    font-size: 17px;
    font-weight: 700;
    transform: translateX(-20px);
  }
</style>
</head>
<body>
<main class="canvas">
  <section class="poster">
    <div class="brand-panel">
      <div class="brand-mark" aria-hidden="true"></div>
      <h1 class="brand-name">
        <span class="line-main">Thornwell</span>
        <span class="line-sub">Building Company</span>
      </h1>
    </div>

    <div class="message-panel">
      <h2 class="headline">
        <span class="lead">Build with the</span>
        <span class="crew">T-CREW!</span>
      </h2>

      <div class="phone-box">
        <svg viewBox="0 0 24 24" aria-hidden="true">
          <path fill="var(--accent-green)" d="M6.6 10.8a15.1 15.1 0 0 0 6.6 6.6l2.2-2.2c.3-.3.7-.4 1-.2 1.1.4 2.3.6 3.6.6.6 0 1 .4 1 1V20c0 .6-.4 1-1 1A17 17 0 0 1 3 4c0-.6.4-1 1-1h3.5c.6 0 1 .4 1 1 0 1.3.2 2.5.6 3.6.1.3 0 .7-.2 1z"/>
        </svg>
        <span class="phone-number">472-555-0188</span>
      </div>

      <ul class="contact-list">
        <li>
          <svg viewBox="0 0 24 24" aria-hidden="true">
            <rect x="2" y="5" width="20" height="14" fill="var(--ink)"/>
            <path d="M2 5l10 8 10-8" fill="none" stroke="var(--brand-green)" stroke-width="1.6"/>
          </svg>
          <span>thornwellbuildingcompany@mailvero.com</span>
        </li>
        <li>
          <svg viewBox="0 0 24 24" aria-hidden="true" fill="none" stroke="var(--ink)" stroke-width="1.8">
            <circle cx="12" cy="12" r="9.5"/>
            <ellipse cx="12" cy="12" rx="4.2" ry="9.5"/>
            <path d="M2.5 12h19M4 7h16M4 17h16"/>
          </svg>
          <span>thornwellbuildingcompany.com</span>
        </li>
      </ul>

      <p class="license">Lic#4620385</p>
    </div>
  </section>
</main>
</body>
</html>
```